I work in the manufacturing industry and currently for TK in the wind department. I'm a contractor. So no TK symbol can be on the card but I can put a wind turbine on it. I am a skydiver as well, so I want a skydiver in the parachute floating next to a turbine with some clouds, the sun over head and the ground below. Hits the moto.

Quality inspection and manufacturing is the industry I work in.

Industry

Walter Denshaw
PXR (manufacturing Quality Inspector)
"Analyzing Quality from a different angle!"

Lark48213@mailbox-example.com
555-302-7184

• Skydiver in parachute, wind turbine, clouds, the sun and the ground. If you can come up with a better moto, please let me know. The back side display "FenLatch inc" in small text in a corner.

```html
<!DOCTYPE html>
<html lang="en">
<head>
<meta charset="UTF-8">
<title>Walter Denshaw – Business Card</title>
<link href="https://fonts.googleapis.com/css2?family=Fira+Sans:wght@400;600;700&display=swap" rel="stylesheet">
<style>
  :root {
    --backdrop: #2a221c;
    --card-top: #124f7e;
    --card-bottom: #0c3e66;
    --ink-soft: #6f9fcc;
    --ink-light: #e9f1f8;
    --ink-muted: #8fb2d3;
    --wave: #3f78aa;
    --wave-pale: #5b8fbf;
    --art-tone: #1d5b8c;
  }
  * { margin: 0; padding: 0; box-sizing: border-box; }
  html, body {
    width: 1200px; height: 900px; overflow: hidden;
    background: var(--backdrop);
    font-family: "Fira Sans", Arial, sans-serif;
  }
  .card-set { position: relative; width: 1200px; height: 900px; }
  .card {
    position: absolute; top: 215px;
    width: 300px; height: 470px;
    background: linear-gradient(160deg, var(--card-top), var(--card-bottom));
    box-shadow: 0 10px 24px rgba(0,0,0,.55);
    overflow: hidden;
  }
  .card--back { left: 255px; }
  .card--front { left: 645px; }
  .waves { position: absolute; left: 0; width: 300px; }
  .card--back .waves { bottom: 0; height: 90px; }
  .card--front .waves { top: 260px; height: 110px; }

  .company-mark {
    position: absolute; right: 26px; bottom: 96px;
    color: var(--ink-soft); font-weight: 600; font-size: 22px; line-height: 1;
    font-variant: small-caps; letter-spacing: .5px;
  }

  .holder { position: absolute; right: 20px; top: 40px; text-align: right; }
  .holder__name {
    color: var(--ink-light); font-weight: 700; font-size: 15px;
    font-variant: small-caps; letter-spacing: .6px;
  }
  .holder__role { color: var(--ink-muted); font-size: 7.5px; margin-top: 2px; }

  .motto {
    position: absolute; left: 40px; right: 30px; top: 98px;
    text-align: center; color: var(--ink-soft);
    font-weight: 700; font-size: 15px; line-height: 1.05;
    font-variant: small-caps; letter-spacing: .8px;
  }
  .scene-art {
    position: absolute; left: 60px; top: 150px; width: 215px; height: 150px;
    background: radial-gradient(ellipse at 60% 50%, var(--art-tone), transparent 72%);
  }
  .contact {
    position: absolute; right: 22px; bottom: 58px;
    list-style: none; color: var(--ink-muted);
    font-weight: 600; font-size: 10px; letter-spacing: .6px;
  }
  .contact li { display: flex; align-items: center; justify-content: flex-end; gap: 8px; margin-top: 5px; }
  .contact svg { width: 9px; height: 10px; flex: none; }
</style>
</head>
<body>
<main class="card-set">
  <section class="card card--back" aria-label="Card back">
    <div class="company-mark">FenLatch inc</div>
    <svg class="waves" viewBox="0 0 300 90" preserveAspectRatio="none" aria-hidden="true">
      <path d="M0 84 C100 76 210 56 300 18 L300 26 C210 64 100 82 0 88Z" fill="var(--wave)"/>
      <path d="M0 90 C110 82 220 64 300 32 L300 40 C220 72 110 88 20 90Z" fill="var(--wave-pale)" opacity=".75"/>
      <path d="M80 90 C170 82 240 68 300 48 L300 55 C240 76 170 88 120 90Z" fill="var(--wave)" opacity=".8"/>
    </svg>
  </section>

  <section class="card card--front" aria-label="Card front">
    <header class="holder">
      <div class="holder__name">Walter Denshaw</div>
      <div class="holder__role">PXR - manufacturing Quality inspector</div>
    </header>
    <p class="motto">Analyzing quality from<br>a different angle</p>
    <div class="scene-art" role="img" aria-label="Line illustration of a sun and cloud, a skydiver under a parachute and a wind turbine"></div>
    <svg class="waves" viewBox="0 0 300 110" preserveAspectRatio="none" aria-hidden="true">
      <path d="M0 70 C90 72 200 50 300 2 L300 14 C200 62 90 82 0 80Z" fill="var(--wave)"/>
      <path d="M0 88 C100 88 210 64 300 22 L300 32 C210 74 100 98 0 97Z" fill="var(--wave-pale)" opacity=".75"/>
      <path d="M0 104 C110 102 220 80 300 42 L300 50 C220 88 110 110 0 110Z" fill="var(--wave)" opacity=".8"/>
    </svg>
    <ul class="contact">
      <li>
        <svg viewBox="0 0 9 10" aria-hidden="true">
          <path d="M2.2 0.8 L3.6 0.8 L4.2 3 L3.2 3.8 C3.7 5 4.5 5.9 5.4 6.4 L6.3 5.5 L8.3 6.2 L8.3 7.8 C8.3 8.6 7.7 9.2 6.9 9.1 C3.8 8.7 1 5.9 0.7 2.5 C0.6 1.6 1.3 0.8 2.2 0.8Z" fill="currentColor"/>
        </svg>
        555-302-7184
      </li>
      <li>
        <svg viewBox="0 0 9 10" aria-hidden="true"><rect x="0.5" y="2" width="8" height="6" fill="none" stroke="currentColor" stroke-width="0.9"/><path d="M0.5 2 L4.5 5.3 L8.5 2" fill="none" stroke="currentColor" stroke-width="0.9"/></svg>
        Lark48213@mailbox-example.com
      </li>
    </ul>
  </section>
</main>
</body>
</html>
```